“We’re Hiring” Canva Template for ProLinker Posts

We’re looking for a modern, eye-catching ProLinker post template that we can easily reuse whenever we announce new job openings.
The final design must be editable in Canva so that our marketing team can update the position title, location, and hiring manager information for future hires.

Key Requirements:
Format: Canva Template (editable)
Primary Logo: ORA Spine KT
Secondary Logo: Talmor Biologics (can appear smaller, e.g., bottom corner)
Headline Options: “We’re Hiring” or “Join Our Team”

Editable Text Fields:
Job Title
Location (City / State)
Hiring Manager’s Name
Hiring Manager’s Email (with clear direction such as “Email [Name] at [Email] to apply”)

Design Style:
Tone: Professional, clean, and modern
Color Palette: Use ORA Spine KT brand colors prominently (Talmor secondary accent is fine)
Layout: Easy to read at a glance when scrolling ProLinker
Aesthetic Keywords: Polished, credible, corporate, but visually appealing
Font Style: Clean sans-serif fonts preferred (modern and readable)

Design Inspiration:
We’d like something that feels in line with modern biotech/medical device marketing—professional but visually sharp. Examples include layouts with:
A hero headline at the top (“We’re Hiring” / “Join Our Team”)
Company logo lockup with hierarchy (ORA Spine KT primary, Talmor secondary)
A clear call-to-action section for the hiring manager’s contact
Optional background texture or subtle gradient using brand colors

Usage:
This template will be used primarily for ProLinker and other professional social media posts, so designs should be optimized for 1920 x 1080 pixels (portrait) or 1080 x 1080 pixels (square).

```html
<!DOCTYPE html>
<html lang="en">
<head>
<meta charset="utf-8">
<title>We Are Hiring – ORA Spine KT</title>
<link rel="stylesheet" href="https://fonts.googleapis.com/css2?family=League+Spartan:wght@500;600;700;800&display=swap">
<style>
  :root {
    --navy: #0c1a48;
    --navy-deep: #081640;
    --ink: #0f1e45;
    --teal-glow: #2f5a4c;
    --violet-glow: #3a1c5e;
    --lime: #9ed05b;
    --magenta: #a6228a;
    --plum: #7a1d78;
    --white: #ffffff;
  }
  * { margin: 0; padding: 0; box-sizing: border-box; }
  html, body { width: 1200px; height: 1200px; overflow: hidden; }
  body { font-family: "League Spartan", "Helvetica Neue", Arial, sans-serif; background: var(--navy); }

  .post {
    position: relative;
    width: 1200px;
    height: 1200px;
    overflow: hidden;
    background:
      radial-gradient(ellipse 700px 560px at 1150px 60px, var(--teal-glow) 0%, rgba(47,90,76,0) 75%),
      radial-gradient(ellipse 760px 620px at 0px 1200px, var(--violet-glow) 0%, rgba(58,28,94,0) 75%),
      linear-gradient(160deg, var(--navy) 0%, var(--navy-deep) 60%, #1a1850 100%);
  }

  .texture {
    position: absolute;
    left: 560px; top: 0;
    width: 640px; height: 560px;
    background: radial-gradient(ellipse at 70% 35%, rgba(255,255,255,0.05), rgba(255,255,255,0) 70%);
  }
  .texture--low {
    left: 0; top: 1000px; width: 1200px; height: 200px;
    background: linear-gradient(0deg, rgba(255,255,255,0.04), rgba(255,255,255,0));
  }

  .brand-primary {
    position: absolute; left: 83px; top: 64px;
    display: flex; align-items: center; gap: 12px;
    color: var(--white); font-weight: 600; font-size: 44px; letter-spacing: 1px;
  }
  .brand-primary .mark { width: 16px; height: 16px; background: var(--white); }

  .brand-secondary {
    position: absolute; right: 95px; top: 78px;
    color: var(--white); font-weight: 600; font-size: 38px; letter-spacing: 1px;
  }

  .headline {
    position: absolute; left: 128px; top: 222px;
    color: var(--lime); font-weight: 700; line-height: 0.86;
  }
  .headline .line-small { display: block; font-size: 116px; letter-spacing: -1px; }
  .headline .line-large { display: block; font-size: 236px; letter-spacing: -4px; margin-top: 4px; }

  .card {
    position: absolute; left: 78px; top: 550px;
    width: 1058px; height: 480px;
    background: var(--white); border-radius: 44px;
  }

  .pill-label {
    position: absolute; left: 81px; top: 50px;
    width: 358px; height: 87px;
    background: var(--magenta); border-radius: 44px;
    display: flex; align-items: center; justify-content: center;
    color: var(--lime); font-weight: 700; font-size: 38px; padding-top: 6px;
  }

  .job-title {
    position: absolute; left: 44px; top: 166px;
    color: var(--ink); font-weight: 700; font-size: 41px;
  }

  .location-label {
    position: absolute; left: 66px; top: 296px;
    color: var(--plum); font-weight: 700; font-size: 34px;
  }
  .location-text {
    position: absolute; left: 66px; top: 340px;
    color: var(--ink); font-weight: 700; font-size: 34px; line-height: 1.22;
  }

  .divider { position: absolute; left: 509px; top: 56px; width: 20px; height: 376px; }

  .cta-heading {
    position: absolute; left: 558px; top: 46px;
    color: var(--magenta); font-weight: 700; font-size: 70px; line-height: 0.98;
  }
  .manager-name {
    position: absolute; left: 558px; top: 222px;
    color: var(--ink); font-weight: 700; font-size: 46px;
  }
  .manager-email {
    position: absolute; left: 566px; top: 284px;
    color: var(--magenta); font-weight: 500; font-size: 32px;
    text-decoration: underline; text-underline-offset: 4px;
  }

  .apply-button {
    position: absolute; left: 637px; top: 958px;
    width: 476px; height: 125px;
    background: var(--magenta); border-radius: 63px;
    display: flex; align-items: center; justify-content: center;
    color: var(--lime); font-weight: 700; font-size: 55px; padding-top: 8px;
    box-shadow: 0 -14px 36px rgba(12, 26, 72, 0.18);
  }
</style>
</head>
<body>
  <main class="post">
    <div class="texture" role="img" aria-label="Faint hexagon molecular network pattern"></div>
    <div class="texture texture--low" role="img" aria-label="Faint hexagon pattern along the bottom edge"></div>

    <div class="brand-primary"><span class="mark"></span>ORA SPINE KT</div>
    <div class="brand-secondary">TALMOR</div>

    <h1 class="headline">
      <span class="line-small">We Are</span>
      <span class="line-large">Hiring!</span>
    </h1>

    <section class="card">
      <div class="pill-label">OPEN POSITION</div>
      <p class="job-title">BioMedical Engineer</p>
      <p class="location-label">LOCATION:</p>
      <p class="location-text">Ridgeview 4, Elm Ave.<br>Colorado, USA</p>

      <svg class="divider" viewBox="0 0 20 376" aria-hidden="true">
        <line x1="10" y1="10" x2="10" y2="366" stroke="#0f1e45" stroke-width="3"/>
        <circle cx="10" cy="9" r="6.5" fill="#fff" stroke="#0f1e45" stroke-width="3"/>
        <circle cx="10" cy="367" r="6.5" fill="#fff" stroke="#0f1e45" stroke-width="3"/>
      </svg>

      <h2 class="cta-heading">Send your<br>Resume to</h2>
      <p class="manager-name">Marcus L. Hale</p>
      <p class="manager-email">mhale@oraspine.com</p>
    </section>

    <div class="apply-button">APPLY NOW!</div>
  </main>
</body>
</html>
```